Project Willow Crest; Retail packaging for handmade bar soap.

A clean design that conveys quality and affordable luxury. Wrapper material is 80 lb felt cover paper, used as a wrap around the product.

Attached is my idea. Logo is purchased. Unless you think it's terrible, maybe best is to refine what I have? I'm thinking fonts, proportions, etc. Honestly though, if you think it's bad we can start from scratch. I think it's good but I'm not that invested in it. I just want to sell good soap.
5 different fragrances, each identical packaging except the colored stripe and the scent name. Should the scent name be inside the colored stripe or above it?

Apologies for the non-metric:
Soap is 3" tall and 2-13/16" wide and 1" deep.
Front of label is 2-5/16" tall and 2-13/16" wide.
Label (wrap) is 8-1/2" long

Looking forward to hearing from you guys.

Target Market(s)

retail gift shops, health food stores, hotel gift shops.

Industry/Entity Type

retail and online personal care products

Other font styles liked:
• not decorative or script

Colors
0054AA
0677BA
7BADD7
CADEEF
E8F1F8
59FF00
82FF00
B8FF75
E3FFCB
F4FFEA
FFF300
FFF600
FEFA6F
FFFEC7
FFFEE8
EB3D1F
EC4F4E
F09395
F8D3D4
FCEDEE
A7469A
B969AE
D3A5CF
EDDBEB
F8F0F9

Requirements
Must have
• The best word I can think of is feng shui. My soap makes you feel good when you use it. It's simple and clean. I want the same in the label.

```html
<!DOCTYPE html>
<html lang="en">
<head>
<meta charset="utf-8">
<title>Willow Crest Soap Co. – Coconut &amp; Lemongrass Wrap</title>
<link rel="stylesheet" href="https://fonts.googleapis.com/css2?family=Bebas+Neue&family=Montserrat:wght@400;500;600;700&display=swap">
<style>
  :root {
    --page-bg: #eceff0;
    --paper: #ffffff;
    --ink: #1f1f1f;
    --teal: #1aa3a0;
    --ocean: #0b64a0;
    --white: #ffffff;
  }
  * { box-sizing: border-box; margin: 0; padding: 0; }
  html, body {
    width: 710px;
    height: 1200px;
    overflow: hidden;
    background: var(--page-bg);
  }
  .canvas {
    width: 710px;
    height: 1200px;
    display: flex;
    flex-direction: column;
    align-items: center;
    justify-content: center;
    gap: 70px;
  }
  .defs { position: absolute; width: 0; height: 0; overflow: hidden; }
  .front-label { width: 520px; height: 416px; display: block; box-shadow: 0 4px 14px rgba(0,0,0,.12); }
  .wrap-flat { width: 670px; height: 221px; display: block; box-shadow: 0 4px 14px rgba(0,0,0,.12); }
  .t-spec { font-family: "Bebas Neue", sans-serif; font-size: 14px; fill: var(--ink); letter-spacing: .5px; }
  .t-brand { font-family: "Bebas Neue", sans-serif; font-size: 27px; fill: var(--ink); letter-spacing: 1.5px; }
  .t-tagline { font-family: "Bebas Neue", sans-serif; font-size: 15px; fill: var(--teal); letter-spacing: 1px; }
  .t-scent { font-family: "Montserrat", sans-serif; font-weight: 600; font-size: 15px; fill: var(--white); letter-spacing: .4px; }
  .t-heading { font-family: "Montserrat", sans-serif; font-weight: 700; font-size: 13px; fill: var(--ink); }
  .t-body { font-family: "Montserrat", sans-serif; font-weight: 400; font-size: 11px; fill: var(--ink); }
  .t-body .lead { font-weight: 600; }
  .t-web { font-family: "Montserrat", sans-serif; font-weight: 600; font-size: 13px; fill: var(--white); }
  .t-slogan { font-family: "Montserrat", sans-serif; font-weight: 400; font-size: 10px; fill: var(--white); }
  .t-side { font-family: "Montserrat", sans-serif; font-weight: 600; font-size: 14px; fill: var(--ink); letter-spacing: .6px; }
</style>
</head>
<body>
<svg class="defs" aria-hidden="true">
  <defs>
    <linearGradient id="band-gradient" x1="0" y1="0" x2="0" y2="1">
      <stop offset="0" stop-color="#1aa3a0"/>
      <stop offset="1" stop-color="#0b5f9c"/>
    </linearGradient>
    <linearGradient id="ornament-gradient" x1="0" y1="0" x2="0" y2="1">
      <stop offset="0" stop-color="#ffffff"/>
      <stop offset="1" stop-color="#8fd3d0"/>
    </linearGradient>
    <symbol id="front-panel" viewBox="0 0 350 280">
      <rect width="350" height="280" fill="#ffffff"/>
      <text class="t-spec" x="18" y="26">100G</text>
      <text class="t-spec" x="332" y="26" text-anchor="end">NET WT. 3.5 OZ.</text>
      <text class="t-brand" x="175" y="66" text-anchor="middle">WILLOW CREST SOAP CO.</text>
      <text class="t-tagline" x="175" y="90" text-anchor="middle">ALL NATURAL &amp; HANDMADE ON THE COAST</text>
      <rect class="ornament" x="0" y="110" width="350" height="90" fill="url(#ornament-gradient)" role="img" aria-label="Ocean wave and curl ornament"/>
      <rect class="scent-band" x="0" y="200" width="350" height="80" fill="url(#band-gradient)"/>
      <text class="t-scent" x="175" y="246" text-anchor="middle">COCONUT &amp; LEMONGRASS</text>
    </symbol>
  </defs>
</svg>

<main class="canvas">
  <svg class="front-label" viewBox="0 0 350 280" role="img" aria-label="Front panel of the soap wrap">
    <use href="#front-panel" width="350" height="280"/>
  </svg>

  <svg class="wrap-flat" viewBox="0 0 1000 330" role="img" aria-label="Full flat soap wrap: back, side, front, side">
    <rect width="1000" height="330" fill="#ffffff"/>

    <g class="panel-back">
      <text class="t-heading" x="30" y="52">INGREDIENTS:</text>
      <text class="t-body" x="30">
        <tspan x="30" y="80"><tspan class="lead">Saponified Oils:</tspan> (Coconut, Olive, Sustain-</tspan>
        <tspan x="30" y="96">able Certified Palm, Cocoa Butter and</tspan>
        <tspan x="30" y="112">Castor oil)</tspan>
        <tspan x="30" y="138"><tspan class="lead">Goodies:</tspan> glycerin, artesian spring water,</tspan>
        <tspan x="30" y="154">white porcelain clay, Oregon honey, fermen-</tspan>
        <tspan x="30" y="170">tation derived natural citric acid and lactic</tspan>
        <tspan x="30" y="186">acid, Oregon sea salt, natural fragrances and</tspan>
        <tspan x="30" y="202">natural earth colorants</tspan>
      </text>
      <rect class="ornament" x="0" y="214" width="350" height="40" fill="url(#ornament-gradient)" role="img" aria-label="Ocean wave ornament"/>
      <rect class="web-band" x="0" y="254" width="350" height="56" fill="url(#band-gradient)"/>
      <circle cx="38" cy="284" r="5.5" fill="none" stroke="#ffffff" stroke-width="1.6"/>
      <text class="t-web" x="50" y="289">WILLOWCREST.US</text>
      <line x1="220" y1="268" x2="220" y2="300" stroke="#ffffff" stroke-width="1.2"/>
      <text class="t-slogan" x="232" y="281">Buy good coffee?</text>
      <text class="t-slogan" x="232" y="295">Buy good soap</text>
    </g>

    <g class="panel-side">
      <text class="t-side" transform="translate(433 235) rotate(-90)">WILLOW CREST SOAP CO.</text>
      <circle cx="428" cy="278" r="10" fill="none" stroke="#1f1f1f" stroke-width="1.2"/>
    </g>

    <use class="panel-front" href="#front-panel" x="505" y="30" width="350" height="280"/>

    <g class="panel-side">
      <text class="t-side" transform="translate(933 235) rotate(-90)">WILLOW CREST SOAP CO.</text>
      <circle cx="928" cy="278" r="10" fill="none" stroke="#1f1f1f" stroke-width="1.2"/>
    </g>
  </svg>
</main>
</body>
</html>
```